Valmora Holdings - Tidal Crest Car Wash automatic car wash signage

We are wanting to have a new automatic car wash sign designed. Our current one is dated and there are numerous options that are no longer available. We like the look of a clean sharp design in keeping with the Tidal Crest colours; orange and blues. The sign should have the Ultimate and Premium options, the "Tidal Crest" and Tidal Crest Car Wash designed in a clean, concise and cool manner.

Font styles to use
Sans Serif

Colors
f37122
3276b5
0255a3
34a7d8

Requirements
Must have
• This project must have the Ultimate and Premium options, the "bucket" and the Tidal Crest Car Wash title. The orange is a key colour with blues for water.

```html
<!DOCTYPE html>
<html lang="en">
<head>
<meta charset="utf-8">
<title>Tidal Crest Car Wash – Menu Sign</title>
<link rel="stylesheet" href="https://fonts.googleapis.com/css2?family=Montserrat:wght@700;800;900&display=swap">
<style>
  :root{
    --orange:#f37122;
    --orange-deep:#e8560f;
    --navy:#13315c;
    --navy-dark:#0e2444;
    --blue:#3276b5;
    --blue-deep:#0255a3;
    --sky:#34a7d8;
    --foam:#cfeefb;
    --page:#1a2333;
    --white:#ffffff;
  }
  *{box-sizing:border-box;margin:0;padding:0}
  html,body{width:720px;height:1200px;overflow:hidden;background:var(--page)}
  body{position:relative;font-family:"Montserrat",sans-serif}

  .sign{position:absolute;left:20px;top:435px;width:680px;height:330px;overflow:hidden;background:var(--foam)}

  .sign__bubbles{position:absolute;inset:0;
    background:radial-gradient(ellipse at 30% 30%,#e6f7fe 0%,#a9def5 45%,#5cc0ea 100%)}

  .sign__waves{position:absolute;inset:0;width:680px;height:330px}

  .sign__photo{position:absolute;left:509px;top:134px;width:171px;height:196px;
    background:linear-gradient(160deg,#d8f0fb 0%,#8fcdf0 40%,#3f8fcf 75%,#cde9f8 100%)}

  .brand{position:absolute;left:56px;top:34px;width:110px;height:110px;display:flex;align-items:center;justify-content:center;flex-direction:column}
  .brand__disc{position:absolute;inset:0;border-radius:50%;background:rgba(52,167,216,.35)}
  .brand__name{position:relative;font-weight:900;font-size:22px;line-height:1;color:var(--orange);text-align:center}

  .title{position:absolute;font-weight:900;color:var(--orange);line-height:1;letter-spacing:-.5px;
    background:var(--navy-dark);padding:4px 8px 6px;text-shadow:3px 3px 0 var(--navy-dark)}
  .title--top{left:225px;top:18px;font-size:46px}
  .title--bottom{left:392px;top:76px;font-size:46px}

  .menu{position:absolute;left:0;top:0;width:680px;height:330px}
  .menu__row{position:absolute;left:27px;width:482px;height:14px;display:flex;align-items:center}
  .menu__row--navy{background:var(--navy)}
  .menu__row--orange{background:var(--orange-deep)}
  .menu__label{width:218px;display:flex;align-items:center;gap:6px;padding-left:4px;
    color:var(--white);font-weight:800;font-size:8.4px;letter-spacing:.1px;white-space:nowrap}
  .menu__icon{width:10px;height:10px;flex:none}
  .menu__tick{width:134px;text-align:center;color:var(--white);font-size:9px;font-weight:700}

  .menu__row:first-of-type{border-radius:7px 0 0 7px}
  .menu__row{border-radius:7px 0 0 7px}

  .plans{position:absolute;left:245px;top:155px;width:264px;height:216px;
    border:2px solid var(--white);border-top:none;border-radius:0 0 12px 12px;pointer-events:none}
  .plans__head{position:absolute;left:245px;top:155px;width:264px;height:23px;display:flex;background:var(--blue)}
  .plans__name{flex:1;display:flex;align-items:center;justify-content:center;color:var(--white);
    font-weight:800;font-size:11.5px;letter-spacing:.2px}
  .plans__name + .plans__name{border-left:1px solid rgba(255,255,255,.35)}
  .plans__name sup{font-size:7px;margin-left:1px}
  .plans__divider{position:absolute;left:378px;top:178px;width:1px;height:140px;background:rgba(255,255,255,.35)}
</style>
</head>
<body>
  <main class="sign">
    <div class="sign__bubbles" role="img" aria-label="Soapy water bubbles background in light blues"></div>

    <svg class="sign__waves" viewBox="0 0 680 330" aria-hidden="true">
      <path d="M0 150 C80 210 160 215 260 170 C360 125 470 120 680 105 L680 160 C520 160 420 175 320 185 C200 200 100 215 0 195 Z" fill="#34a7d8" opacity=".55"/>
      <path d="M40 205 C120 225 200 215 300 185 C420 150 540 140 680 165 L680 190 C560 170 460 175 360 195 C250 215 150 230 60 225 Z" fill="#0255a3"/>
    </svg>

    <div class="sign__photo" role="img" aria-label="Photo of a car side mirror and window being washed"></div>

    <div class="brand">
      <span class="brand__disc"></span>
      <span class="brand__name">Tidal<br>Crest</span>
    </div>

    <h1>
      <span class="title title--top">Tidal Crest</span>
      <span class="title title--bottom">Car Wash</span>
    </h1>

    <section class="menu">
      <div class="plans__head">
        <div class="plans__name">ULTIMATE $14<sup>00</sup></div>
        <div class="plans__name">PREMIUM $12<sup>00</sup></div>
      </div>

      <div class="menu__row menu__row--navy" style="top:178px"><span class="menu__label"><svg class="menu__icon" viewBox="0 0 10 10"><circle cx="5" cy="5" r="4.2" fill="none" stroke="#fff" stroke-width="1"/><path d="M3 5.2l1.5 1.4L7.2 3.6" fill="none" stroke="#fff" stroke-width="1"/></svg>WINDSHIELD &amp; FRONT END BUG WASH</span><span class="menu__tick">✓</span><span class="menu__tick">✓</span></div>
      <div class="menu__row menu__row--orange" style="top:192px"><span class="menu__label"><svg class="menu__icon" viewBox="0 0 10 10"><circle cx="5" cy="5" r="4.2" fill="none" stroke="#fff" stroke-width="1"/><path d="M3 5.2l1.5 1.4L7.2 3.6" fill="none" stroke="#fff" stroke-width="1"/></svg>UNDER CARRIAGE &amp; WHEEL BLASTER</span><span class="menu__tick">✓</span><span class="menu__tick">✓</span></div>
      <div class="menu__row menu__row--navy" style="top:206px"><span class="menu__label"><svg class="menu__icon" viewBox="0 0 10 10"><circle cx="5" cy="5" r="4.2" fill="none" stroke="#fff" stroke-width="1"/><path d="M3 5.2l1.5 1.4L7.2 3.6" fill="none" stroke="#fff" stroke-width="1"/></svg>EXTRA PASS OF HIGH PRESSURE WASH</span><span class="menu__tick">✓</span><span class="menu__tick">✓</span></div>
      <div class="menu__row menu__row--orange" style="top:220px"><span class="menu__label"><svg class="menu__icon" viewBox="0 0 10 10"><circle cx="5" cy="5" r="4.2" fill="none" stroke="#fff" stroke-width="1"/><path d="M3 5.2l1.5 1.4L7.2 3.6" fill="none" stroke="#fff" stroke-width="1"/></svg>TRY FOAM CONDITIONER / CLEANER</span><span class="menu__tick">✓</span><span class="menu__tick">✓</span></div>
      <div class="menu__row menu__row--navy" style="top:234px"><span class="menu__label"><svg class="menu__icon" viewBox="0 0 10 10"><circle cx="5" cy="5" r="4.2" fill="none" stroke="#fff" stroke-width="1"/><path d="M3 5.2l1.5 1.4L7.2 3.6" fill="none" stroke="#fff" stroke-width="1"/></svg>SIDE KICK DRYERS</span><span class="menu__tick">✓</span><span class="menu__tick">✓</span></div>
      <div class="menu__row menu__row--orange" style="top:248px"><span class="menu__label"><svg class="menu__icon" viewBox="0 0 10 10"><circle cx="5" cy="5" r="4.2" fill="none" stroke="#fff" stroke-width="1"/><path d="M3 5.2l1.5 1.4L7.2 3.6" fill="none" stroke="#fff" stroke-width="1"/></svg>WAX / SURFACE PROTECTANT</span><span class="menu__tick">✓</span><span class="menu__tick">✓</span></div>
      <div class="menu__row menu__row--navy" style="top:262px"><span class="menu__label"><svg class="menu__icon" viewBox="0 0 10 10"><circle cx="5" cy="5" r="4.2" fill="none" stroke="#fff" stroke-width="1"/><path d="M3 5.2l1.5 1.4L7.2 3.6" fill="none" stroke="#fff" stroke-width="1"/></svg>ON BOARD OVERHEAD DRYER</span><span class="menu__tick">✓</span><span class="menu__tick">✓</span></div>
      <div class="menu__row menu__row--orange" style="top:276px"><span class="menu__label"><svg class="menu__icon" viewBox="0 0 10 10"><circle cx="5" cy="5" r="4.2" fill="none" stroke="#fff" stroke-width="1"/><path d="M3 5.2l1.5 1.4L7.2 3.6" fill="none" stroke="#fff" stroke-width="1"/></svg>TWO PASSES OF PRE-SOAK</span><span class="menu__tick">✓</span><span class="menu__tick">✓</span></div>
      <div class="menu__row menu__row--navy" style="top:290px"><span class="menu__label"><svg class="menu__icon" viewBox="0 0 10 10"><circle cx="5" cy="5" r="4.2" fill="none" stroke="#fff" stroke-width="1"/><path d="M3 5.2l1.5 1.4L7.2 3.6" fill="none" stroke="#fff" stroke-width="1"/></svg>HIGH PRESSURE WASH PASS</span><span class="menu__tick">✓</span><span class="menu__tick">✓</span></div>
      <div class="menu__row menu__row--orange" style="top:304px"><span class="menu__label"><svg class="menu__icon" viewBox="0 0 10 10"><circle cx="5" cy="5" r="4.2" fill="none" stroke="#fff" stroke-width="1"/><path d="M3 5.2l1.5 1.4L7.2 3.6" fill="none" stroke="#fff" stroke-width="1"/></svg>SPOT FREE RIMSE</span><span class="menu__tick">✓</span><span class="menu__tick">✓</span></div>

      <div class="plans__divider"></div>
      <div class="plans" style="height:170px"></div>
    </section>
  </main>
</body>
</html>
```